Silver Creek Plumbing Business card & letter head design

We need a new business card and letter head for our plumbing company called silver creek plumbing. attached is the companys logo. We provide domestic and commercial plumbing services in regional western Australia. We are after Something simple yet nice to look at and something that fits within the trade industry.

Target Market(s)

trade/building industry

Contact Information for Business Card

Darl Hensby
Manager
0461 238 574
enquiries@scplumbwork.net.au
ABN: 47 381 905 462
PCL: 5187

Domestic & Commercial Plumbing
Tip Truck & Excavator hire

Colors

Designer to choose colors to be used in the design.

```html
<!DOCTYPE html>
<html lang="en">
<head>
<meta charset="utf-8">
<title>Silver Creek Plumbing – Stationery</title>
<link rel="stylesheet" href="https://fonts.googleapis.com/css2?family=Source+Sans+3:wght@400;600;700&display=swap">
<style>
  :root{
    --brand-blue:#0e56a0;
    --charcoal:#545454;
    --paper:#f5f5f5;
    --backdrop:#e3e3e4;
    --text-grey:#4a4a4a;
    --faint-blue:#dfe5ee;
  }
  *{box-sizing:border-box;margin:0;padding:0}
  html,body{width:1200px;height:1200px;overflow:hidden}
  body{background:var(--backdrop);font-family:"Source Sans 3",Arial,sans-serif;position:relative;color:var(--text-grey)}

  .sheet{position:absolute;background:var(--paper);box-shadow:2px 3px 6px rgba(0,0,0,.25);overflow:hidden}

  .letterhead{left:104px;top:119px;width:682px;height:964px}
  .letterhead .brand{position:absolute;left:54px;top:62px;width:180px;text-align:center;color:var(--brand-blue);font-weight:700;font-size:21px;line-height:1.05;letter-spacing:.5px;text-transform:uppercase}
  .contact-list{position:absolute;left:478px;top:43px;font-size:11px;line-height:14px;list-style:none}
  .contact-list li{display:flex;align-items:center;gap:5px}
  .contact-list svg{width:10px;height:10px;flex:none}
  .reg{position:absolute;left:478px;top:92px;font-size:11px;line-height:14px}
  .reg b{color:var(--brand-blue);font-weight:400}
  .watermark{position:absolute;left:0;top:370px;width:682px;text-align:center;font-weight:700;font-size:66px;line-height:1.05;color:var(--faint-blue);text-transform:uppercase;letter-spacing:1px}
  .footer-wave{position:absolute;left:0;top:0;width:682px;height:964px}
  .tagline{position:absolute;left:0;top:936px;width:682px;text-align:center;color:#fff;font-size:10.5px;text-transform:uppercase}

  .card-front{left:821px;top:248px;width:292px;height:178px;background:var(--brand-blue)}
  .card-front .brand{position:absolute;left:0;top:62px;width:292px;text-align:center;color:#fff;font-weight:700;font-size:16px;line-height:1.05;text-transform:uppercase;letter-spacing:.4px}
  .card-front .web{position:absolute;left:0;top:153px;width:292px;text-align:center;color:#fff;font-size:7px;letter-spacing:1px}

  .card-back{left:821px;top:489px;width:292px;height:178px;background:var(--paper)}
  .card-back .curve{position:absolute;left:0;top:0;width:292px;height:178px}
  .card-back .brand{position:absolute;left:10px;top:68px;width:108px;text-align:center;color:var(--brand-blue);font-weight:700;font-size:12.5px;line-height:1.05;text-transform:uppercase}
  .details{position:absolute;left:169px;top:47px;color:#fff;font-size:6.5px;line-height:10px}
  .details .name{font-size:10.5px;font-weight:700;line-height:12px}
  .details .role{margin-bottom:7px}
  .details ul{list-style:none;margin-bottom:5px}
  .details li{display:flex;align-items:center;gap:4px}
  .details svg{width:6px;height:6px;flex:none}
</style>
</head>
<body>

<section class="sheet letterhead">
  <div class="brand">Silver Creek<br>Plumbing</div>
  <ul class="contact-list">
    <li><svg viewBox="0 0 10 10"><path d="M2 0.5l2 2-1 1.2c.6 1.3 1.5 2.2 2.8 2.8l1.2-1 2 2-1.3 1.5C4 8.7 1.2 6 .5 1.8z" fill="var(--brand-blue)"/></svg>0461 238 574</li>
    <li><svg viewBox="0 0 10 10"><rect x=".7" y="2" width="8.6" height="6" fill="none" stroke="var(--brand-blue)" stroke-width="1.2"/><path d="M.7 2L5 5.5 9.3 2" fill="none" stroke="var(--brand-blue)" stroke-width="1.2"/></svg>enquiries@scplumbwork.net.au</li>
    <li><svg viewBox="0 0 10 10"><circle cx="5" cy="5" r="4.3" fill="none" stroke="var(--brand-blue)"/><ellipse cx="5" cy="5" rx="1.8" ry="4.3" fill="none" stroke="var(--brand-blue)"/><path d="M.7 5h8.6" stroke="var(--brand-blue)"/></svg>www.scplumbwork.net.au</li>
  </ul>
  <div class="reg"><b>ABN:</b> 47 381 905 462<br><b>PCL:</b> 5187</div>
  <div class="watermark" aria-hidden="true">Silver Creek<br>Plumbing</div>
  <svg class="footer-wave" viewBox="0 0 682 964" aria-hidden="true">
    <path d="M0 859 Q340 990 682 831 L682 866 Q340 994 0 862 Z" fill="var(--charcoal)"/>
    <path d="M0 866 Q340 1000 682 871 L682 964 L0 964 Z" fill="var(--brand-blue)"/>
  </svg>
  <p class="tagline">Domestic &amp; Commercial Plumbing • Tip Truck &amp; Excavator Hire</p>
</section>

<section class="sheet card-front">
  <div class="brand">Silver Creek<br>Plumbing</div>
  <p class="web">www.<b>scplumbwork</b>.net.au</p>
</section>

<section class="sheet card-back">
  <svg class="curve" viewBox="0 0 292 178" aria-hidden="true">
    <path d="M123 0 Q172 90 109 178 L127 178 Q168 90 125 0 Z" fill="var(--charcoal)"/>
    <path d="M128 0 Q176 90 131 178 L292 178 L292 0 Z" fill="var(--brand-blue)"/>
  </svg>
  <div class="brand">Silver Creek<br>Plumbing</div>
  <div class="details">
    <p class="name">Darl Hensby</p>
    <p class="role">Manager</p>
    <ul>
      <li><svg viewBox="0 0 10 10"><path d="M2 0.5l2 2-1 1.2c.6 1.3 1.5 2.2 2.8 2.8l1.2-1 2 2-1.3 1.5C4 8.7 1.2 6 .5 1.8z" fill="#fff"/></svg>0461 238 574</li>
      <li><svg viewBox="0 0 10 10"><rect x=".7" y="2" width="8.6" height="6" fill="none" stroke="#fff" stroke-width="1.2"/><path d="M.7 2L5 5.5 9.3 2" fill="none" stroke="#fff" stroke-width="1.2"/></svg>enquiries@scplumbwork.net.au</li>
      <li><svg viewBox="0 0 10 10"><circle cx="5" cy="5" r="4.3" fill="none" stroke="#fff"/><ellipse cx="5" cy="5" rx="1.8" ry="4.3" fill="none" stroke="#fff"/><path d="M.7 5h8.6" stroke="#fff"/></svg>www.scplumbwork.net.au</li>
    </ul>
    <p>ABN: 47 381 905 462<br>PCL: 5187</p>
  </div>
</section>

</body>
</html>
```